Business Cards for Demolition & Salvage Company

We are Licensed Demolition Contractors and this business card design is for our Salvage Yard. We recycle over 95% of the building materials removed from each demolition site in which we take to our Salvage Yard for resale eg. bricks, windows, doors, kitchens, stoves, lights, fencing etc so pretty much everything.
Updates

I forgot to note that single sided business card only please.

Reason: I would like to ask if designers could please submit or re-submit their designs edited to a single sided card only. The card also does not need space for an employee name or position as our general business contact details will suffice for this project. Primary colour must be ROYAL BLUE with no exceptions please. Much appreciated and thank you to all whom have submitted designs to date and I look forward to receiving your edited designs..

Industry/Entity Type

Building

Contact Information for Business Card

Tavelund Demolition & Salvage (WA) Pty Ltd
2413 Coralbrook Parkway
LOWER FENWICK WA 6072
P: (08) 9371 5068
F: (08) 9371 7725
E: salvage@tvwreck.com.au
W: tavelunddemolition.com.au

Requirements
Must have
• We have a logo that has been with our Company since 1974 so he must be included in the design - file attached. As for colours, we have always used royal blue and again this must be the primary colour used in the design. Please keep the design simple.
Nice to have
• Card can include opening hours as follows:
Opening Hours:
Monday to Friday 8am - 5.00pm
Saturday 8am - 3pm
Closed Sunday's and public holidays

```html
<!DOCTYPE html>
<html lang="en">
<head>
<meta charset="utf-8">
<title>Tavelund Demolition &amp; Salvage – Business Card</title>
<link rel="stylesheet" href="https://fonts.googleapis.com/css2?family=Arvo:wght@700&family=Open+Sans:wght@400;600&display=swap">
<style>
  :root {
    --page-bg: #d9d4cc;
    --royal-blue: #1d3f99;
    --royal-blue-deep: #10296f;
    --mascot-light: #6e8fd0;
    --mascot-mid: #4a6bb8;
    --name-white: #eef2fb;
    --text-white: #f4f6fc;
    --hours-pink: #d45fb6;
    --hours-pink-deep: #c24aa6;
    --address-gold: #c9b35a;
  }
  * { box-sizing: border-box; margin: 0; padding: 0; }
  html, body {
    width: 1200px;
    height: 1023px;
    overflow: hidden;
    background: var(--page-bg);
  }
  .canvas {
    position: relative;
    width: 1200px;
    height: 1023px;
    display: flex;
    align-items: center;
    justify-content: center;
  }
  .business-card {
    position: relative;
    width: 1000px;
    height: 571px;
    border-radius: 44px;
    overflow: hidden;
    background: linear-gradient(160deg, var(--royal-blue) 0%, var(--royal-blue-deep) 100%);
    font-family: "Open Sans", Arial, sans-serif;
    color: var(--text-white);
  }
  .mascot-area {
    position: absolute;
    left: 40px;
    top: 235px;
    width: 430px;
    height: 305px;
    border-radius: 40px;
    background: radial-gradient(ellipse at 40% 45%, var(--mascot-light) 0%, var(--mascot-mid) 60%, var(--royal-blue) 100%);
  }
  .company-name {
    position: absolute;
    left: 330px;
    top: 48px;
    font-family: "Arvo", Georgia, serif;
    font-weight: 700;
    font-size: 78px;
    letter-spacing: 3px;
    color: var(--name-white);
    line-height: 1;
  }
  .company-tagline {
    position: absolute;
    left: 338px;
    top: 138px;
    font-size: 30px;
    color: var(--text-white);
    line-height: 1;
  }
  .contact-list {
    position: absolute;
    left: 560px;
    top: 186px;
    list-style: none;
    font-size: 21px;
    line-height: 28px;
  }
  .contact-list .label { font-weight: 600; }
  .opening-hours {
    position: absolute;
    left: 525px;
    top: 318px;
    right: 0;
    height: 150px;
    padding: 22px 0 0 36px;
    border-radius: 40px 0 0 40px;
    background: linear-gradient(180deg, var(--hours-pink) 0%, var(--hours-pink-deep) 100%);
    font-size: 21px;
    line-height: 27px;
  }
  .street-address {
    position: absolute;
    left: 520px;
    bottom: 34px;
    font-size: 19px;
    color: var(--address-gold);
    white-space: nowrap;
  }
</style>
</head>
<body>
  <main class="canvas">
    <article class="business-card">
      <div class="mascot-area" role="img" aria-label="Company mascot illustration: hard-hatted demolition worker swinging a sledgehammer with lightning bolts"></div>

      <h1 class="company-name">TAVELUND</h1>
      <p class="company-tagline">Demolition &amp; Salvage (WA) Pty Ltd</p>

      <ul class="contact-list">
        <li><span class="label">[P]:</span> (08) 9371 5068</li>
        <li><span class="label">[F]:</span> (08) 9371 7725</li>
        <li><span class="label">[E]:</span> salvage@tvwreck.com.au</li>
        <li><span class="label">[W]:</span> tavelunddemolition.com.au</li>
      </ul>

      <section class="opening-hours">
        <p>Opening Hours:</p>
        <p>Monday to Friday 8am - 5.00pm</p>
        <p>Saturday 8am - 3pm</p>
        <p>Closed Sunday's and public holidays</p>
      </section>

      <p class="street-address">2413 Coralbrook Parkway LOWER FENWICK WA 6072</p>
    </article>
  </main>
</body>
</html>
```